Card Design for my dog training business Rustpaw Obedience

Need a business card design for my dog training business with my new logo. Want the card to come off professional yet fun. Want it to be very eye catchy as well. I normally have these at vet clinics, pet stores, and groomers. so need it to look better than my competitors.
Target Market(s)
dog owners
Industry/Entity Type
Dog Training
Contact Information for Business Card
needs logo, my name and info
Font styles to use
Serif
Colors
0255a3
ffffff
ec1f27
000000
333333
fbfbfb
Requirements
Must have
- Rustpaw Obedience
- Hollis Brandt
- 415 903 2267
- info@rustpawobedience.example
- www.rustpawobedience.example

```html
<!DOCTYPE html>
<html lang="en">
<head>
<meta charset="utf-8">
<title>Rustpaw Obedience — Business Card</title>
<link rel="stylesheet" href="https://fonts.googleapis.com/css2?family=EB+Garamond:ital,wght@0,400;0,500;1,400&family=Montserrat:wght@400;500;600&display=swap">
<style>
  :root {
    --brand-blue: #0255a3;
    --brand-red: #ec1f27;
    --ink: #000000;
    --charcoal: #333333;
    --card-black: #1b1c1e;
    --paper: #fbfbfb;
    --white: #ffffff;
    --silver: #d9d9d9;
    --stage: #e9e9eb;
  }
  * { box-sizing: border-box; margin: 0; padding: 0; }
  html, body {
    width: 1200px;
    height: 900px;
    overflow: hidden;
    background: var(--stage);
  }
  .stage {
    position: relative;
    width: 1200px;
    height: 900px;
    display: flex;
    flex-direction: column;
    align-items: center;
    justify-content: center;
    gap: 56px;
  }
  .card {
    position: relative;
    width: 588px;
    height: 336px;
    overflow: hidden;
    box-shadow: 0 10px 28px rgba(0,0,0,0.18);
  }

  /* Back of card */
  .card-back {
    background: var(--card-black);
    color: var(--silver);
    font-family: "EB Garamond", Georgia, serif;
  }
  .card-back .brand-name {
    position: absolute;
    left: 0; right: 0;
    top: 118px;
    text-align: center;
    font-size: 40px;
    font-weight: 400;
    letter-spacing: 1px;
    color: var(--silver);
  }
  .card-back .tagline {
    position: absolute;
    left: 0; right: 0;
    bottom: 62px;
    text-align: center;
    font-style: italic;
    font-size: 24px;
    color: var(--silver);
  }

  /* Front of card */
  .card-front {
    background: var(--paper);
    font-family: "Montserrat", Arial, sans-serif;
  }
  .corner-wedge {
    position: absolute;
    left: 0; top: 0;
    width: 140px;
    height: 336px;
  }
  .dog-illustration {
    position: absolute;
    left: 22px;
    top: 92px;
    width: 290px;
    height: 244px;
    border-radius: 60px 110px 0 0;
    background: linear-gradient(90deg, rgba(2,85,163,0.85) 0%, rgba(2,85,163,0.35) 48%, rgba(236,31,39,0.35) 58%, rgba(236,31,39,0.8) 100%);
  }
  .holder-name {
    position: absolute;
    left: 150px;
    top: 64px;
    font-size: 17px;
    font-weight: 600;
    letter-spacing: 0.5px;
    color: var(--brand-blue);
  }
  .front-brand {
    position: absolute;
    right: 30px;
    top: 104px;
    font-family: "EB Garamond", Georgia, serif;
    font-size: 26px;
    font-weight: 500;
    color: var(--ink);
    text-align: right;
  }
  .contact-list {
    position: absolute;
    right: 30px;
    top: 170px;
    list-style: none;
    font-size: 12px;
    color: var(--charcoal);
    text-align: right;
  }
  .contact-list li {
    display: flex;
    justify-content: flex-end;
    align-items: center;
    gap: 8px;
    margin-bottom: 8px;
  }
  .contact-list svg { width: 12px; height: 12px; flex: none; }
</style>
</head>
<body>
<main class="stage">

  <section class="card card-back" aria-label="Business card back">
    <p class="brand-name">Rustpaw Obedience</p>
    <p class="tagline">“Training dogs across Texas one dog at a time.”</p>
  </section>

  <section class="card card-front" aria-label="Business card front">
    <svg class="corner-wedge" viewBox="0 0 140 336" aria-hidden="true">
      <polygon points="0,0 140,0 0,300" fill="var(--card-black)"/>
      <rect x="0" y="0" width="22" height="336" fill="var(--card-black)"/>
    </svg>
    <div class="dog-illustration" role="img" aria-label="Line illustration of two dog heads, one in blue and one in red"></div>

    <h1 class="holder-name">HOLLIS BRANDT</h1>
    <p class="front-brand">Rustpaw Obedience</p>

    <ul class="contact-list">
      <li>415 903 2267
        <svg viewBox="0 0 12 12" aria-hidden="true"><path d="M3 1 L5 3.5 L4 4.7 C4.6 6 5.8 7.3 7.2 8 L8.4 7 L11 9 L10 11 C5.5 11 1 6.5 1 2 Z" fill="var(--brand-blue)"/></svg>
      </li>
      <li>info@rustpawobedience.example
        <svg viewBox="0 0 12 12" aria-hidden="true"><rect x="0.5" y="2.5" width="11" height="7" fill="var(--brand-blue)"/><path d="M0.5 2.5 L6 6.8 L11.5 2.5" fill="none" stroke="var(--white)" stroke-width="1"/></svg>
      </li>
      <li>www.rustpawobedience.example
        <svg viewBox="0 0 12 12" aria-hidden="true"><circle cx="6" cy="6" r="5.5" fill="var(--brand-blue)"/><path d="M0.5 6 H11.5 M6 0.5 V11.5 M6 0.5 C3 3 3 9 6 11.5 M6 0.5 C9 3 9 9 6 11.5" fill="none" stroke="var(--white)" stroke-width="0.7"/></svg>
      </li>
    </ul>
  </section>

</main>
</body>
</html>
```